Varden Hub, LLC. is the name of the company that will be an Internet startup working in E-commerce and

We are a new company and going to start the business by hiring people we need. We are on “Hiring Now…” status right now which we like to be displayed on the website homepage.
The website should allow us to start the hiring process with letting people see and apply for jobs posted on the website.

the company logo is attached.

Target Market(s)

Tech Job Seekers, Programmers, iOS and Android Developers, Software engineers, Graphic designers, QA engineers, Customer Service Reps,...

Industry/Entity Type

Internet

Number of Pages Required

5+ page

Font styles to use
Serif
Sans Serif

Colors

Designer to choose colors to be used in the design.

Requirements
Must have
• We need a system to help job seekers to upload the resume and cover letter and fill the required forms and answer some questions on a form designed to evaluate the job seekers and let them know if they fit in the position and should apply for it.
• We also want job seekers to do a Pre-Employment Tests including Aptitude, Personality, and Skills after they qualified for a job which links our website to web-based pre-employment testing services websites like (Metrica, Talvex, Brunholt & Partners, Dovin Evaluation, …)

```html
<!DOCTYPE html>
<html lang="en">
<head>
<meta charset="utf-8">
<title>Varden Hub — Hiring Now</title>
<link rel="stylesheet" href="https://fonts.googleapis.com/css2?family=Poppins:wght@300;400;500;600;700&display=swap">
<style>
:root{
  --blue:#1b9ce5;
  --blue-dark:#1284c6;
  --orange:#f07f1f;
  --ink:#222;
  --text:#555;
  --grey-btn:#9c9c9c;
  --footer:#1f1f1f;
  --footer-line:#3a3a3a;
  --white:#fff;
}
*{box-sizing:border-box;margin:0;padding:0}
html,body{width:1200px;height:3737px;overflow:hidden}
body{font-family:'Poppins',sans-serif;color:var(--text);background:var(--white);position:relative}
a{color:inherit;text-decoration:none}
.abs{position:absolute}

/* hero */
.hero{position:absolute;left:0;top:0;width:1200px;height:668px;overflow:hidden}
.hero-photo{position:absolute;inset:0;background:linear-gradient(100deg,#6f7f8c 0%,#8b8e90 35%,#5a5c60 60%,#9aa1a6 100%)}
.hero-shade{position:absolute;inset:0;background:linear-gradient(180deg,rgba(0,0,0,.05),rgba(0,0,0,.25))}
.brand-corner{position:absolute;left:0;top:0;width:400px;height:105px;background:var(--white);clip-path:polygon(0 0,100% 0,78% 100%,0 100%)}
.brand{position:absolute;left:67px;top:18px;display:flex;align-items:center;gap:10px;font-weight:700;font-size:44px;color:var(--blue);letter-spacing:1px}
.brand .dot{width:30px;height:30px;border-radius:50%;background:var(--blue)}
.top-links{position:absolute;left:570px;top:14px;font-size:13px;font-weight:600;color:var(--white);letter-spacing:.5px}
.top-phone{position:absolute;left:800px;top:10px;font-size:17px;font-weight:600;color:var(--white)}
.work-btn{position:absolute;left:976px;top:0;width:154px;height:40px;background:var(--blue);color:var(--white);font-size:13px;font-weight:700;display:flex;align-items:center;justify-content:center}
.nav{position:absolute;left:574px;top:60px;display:flex;gap:24px;font-size:15px;color:var(--white);white-space:nowrap}
.nav .active{color:var(--blue)}
.socials-top{position:absolute;left:992px;top:64px;display:flex;gap:12px}
.socials-top span{width:16px;height:16px;border-radius:50%;background:var(--white)}
.hero-title{position:absolute;left:150px;top:262px;font-size:56px;font-weight:700;color:var(--white)}
.hero-text{position:absolute;left:150px;top:322px;width:500px;font-size:15px;line-height:29px;color:var(--white)}
.btn{display:inline-flex;align-items:center;justify-content:center;font-weight:600;font-size:13px;letter-spacing:.5px;color:var(--white);background:var(--blue);white-space:nowrap}
.hero-btn{position:absolute;left:152px;top:444px;width:180px;height:38px}
.search-band{position:absolute;left:0;top:579px;width:1200px;height:89px;background:rgba(45,45,45,.72)}
.field{position:absolute;top:22px;height:43px;border:1px solid rgba(255,255,255,.8);color:#ddd;font-size:14px;padding:0 14px;display:flex;align-items:center;justify-content:space-between}
.search-btn{position:absolute;left:931px;top:22px;width:122px;height:43px;gap:8px;font-size:14px}

/* features */
.feature{position:absolute;top:766px;width:290px}
.feature h3{display:flex;align-items:center;gap:10px;font-size:20px;font-weight:600;color:var(--ink);white-space:nowrap;height:36px}
.feature p{margin-top:20px;font-size:13px;line-height:30px;width:270px}
.feature .btn{margin-top:22px;width:130px;height:33px;font-size:11px}

/* section headings */
.section-title{position:absolute;left:0;width:1200px;text-align:center;font-size:35px;font-weight:600;color:var(--ink)}
.section-title em{font-style:normal;color:var(--blue)}
.section-lead{position:absolute;left:0;width:1200px;text-align:center;font-size:14px;line-height:26px}

/* jobs */
.job{position:absolute;width:215px}
.job .photo{height:162px}
.job h4{margin-top:30px;font-size:15px;font-weight:600;color:var(--ink);white-space:nowrap}
.job .tag{display:flex;align-items:center;gap:6px;font-size:11px;margin-top:2px}
.job .tag i{width:9px;height:11px;background:var(--orange);clip-path:polygon(0 0,100% 0,100% 100%,50% 70%,0 100%)}
.job p{margin-top:4px;font-size:14.5px;line-height:29px}
.job .actions{display:flex;margin-top:12px;height:35px}
.job .actions a{flex:1;font-size:12px}
.job .actions .view{background:var(--grey-btn)}

/* cta */
.cta{position:absolute;left:0;top:2068px;width:1200px;height:98px;background:var(--orange)}
.cta p{position:absolute;left:232px;top:35px;font-size:19px;color:var(--white)}
.cta a{position:absolute;left:823px;top:32px;width:146px;height:35px;border:2px solid var(--white);color:var(--white);font-size:12px;font-weight:600}

/* testimonial */
.quote{position:absolute;left:0;top:2166px;width:1200px;height:474px;overflow:hidden}
.quote-photo{position:absolute;inset:0;background:linear-gradient(90deg,#3f3a35,#6a6058 40%,#8c8a86 60%,#4d4a46)}
.quote-shade{position:absolute;inset:0;background:rgba(0,0,0,.35)}
.avatar{position:absolute;left:558px;top:107px;width:84px;height:84px;border-radius:50%;background:#c9a891;border:3px solid var(--white)}
.quote p{position:absolute;left:300px;top:222px;width:600px;text-align:center;color:var(--white);font-size:17px;line-height:30px}
.quote .who{position:absolute;left:0;top:330px;width:1200px;text-align:center;color:var(--white);font-weight:600;font-size:17px}
.dots{position:absolute;left:585px;top:379px;display:flex;gap:8px}
.dots span{width:7px;height:7px;border-radius:50%;background:rgba(255,255,255,.5)}
.dots .on{background:var(--blue)}

/* news */
.news{position:absolute;width:468px}
.news .photo{height:212px}
.news .meta{display:flex;margin-top:35px}
.news .date{flex:none;width:96px;text-align:right;font-size:17px;font-weight:600;color:var(--ink);line-height:28px;padding-right:14px;border-right:1px solid #999;white-space:nowrap}
.news .excerpt{padding-left:16px;font-size:13.5px;line-height:27px}

/* footer */
.footer{position:absolute;left:0;top:3194px;width:1200px;height:543px;background:var(--footer);color:#ddd}
.footer h5{font-size:17px;font-weight:600;color:var(--blue)}
.footer h6{font-size:17px;font-weight:600;color:var(--white)}
.news-input{position:absolute;left:150px;top:112px;width:213px;height:38px;background:var(--white);color:#aaa;font-size:13px;padding:0 12px;display:flex;align-items:center}
.news-btn{position:absolute;left:363px;top:112px;width:120px;height:38px;gap:6px}
.footer-socials{position:absolute;left:536px;top:117px;display:flex;gap:14px}
.footer-socials span{width:29px;height:29px;border-radius:50%;border:2px solid var(--blue)}
.footer-rule{position:absolute;left:150px;top:189px;width:910px;height:1px;background:var(--footer-line)}
.links{position:absolute;top:265px;list-style:none;font-size:13.5px}
.links li{height:35px;display:flex;gap:10px;align-items:flex-start}
.links li::before{content:"";margin-top:6px;border-left:7px solid var(--white);border-top:4px solid transparent;border-bottom:4px solid transparent}
.links .hl{color:var(--blue)}
.contact-field{position:absolute;left:822px;width:237px;height:32px;background:#e7e7e7;color:#999;font-size:11px;padding:8px 12px}
.copyright{position:absolute;left:0;top:476px;width:1200px;text-align:center;font-size:11px;color:#bbb}
</style>
</head>
<body>

<header class="hero">
  <div class="hero-photo" role="img" aria-label="Team of smiling office professionals in business attire"></div>
  <div class="hero-shade"></div>
  <div class="brand-corner"></div>
  <div class="brand"><span>VARDEN</span><span class="dot"></span></div>
  <div class="top-links">HELP CENTER &nbsp;|&nbsp; MY ACCOUNT</div>
  <div class="top-phone">&#9990; 1800-0000-5678</div>
  <a class="work-btn" href="#">WORK WITH US!</a>
  <nav class="nav"><a class="active" href="#">Home</a><a href="#">Jobs</a><a href="#">Resume</a><a href="#">About</a><a href="#">Contact Us</a></nav>
  <div class="socials-top"><span></span><span></span><span></span><span></span><span></span></div>
  <h1 class="hero-title">HIRING NOW!</h1>
  <p class="hero-text">Lorem ipsum dolor sit amet consectetur adipisicing labore et dolore magna aliqua uat veniamq icing elit sed do eiusmod temp incidunt ut laboret.</p>
  <a class="btn hero-btn" href="#">CREATE A RESUME</a>
  <div class="search-band">
    <div class="field" style="left:150px;width:244px">Industry (All) <span>&#8964;</span></div>
    <div class="field" style="left:414px;width:247px">Job Type <span>&#8964;</span></div>
    <div class="field" style="left:679px;width:237px">Type search</div>
    <a class="btn search-btn" href="#"><svg width="16" height="14" viewBox="0 0 16 14"><path d="M0 6 16 0 12 14 8 9 14 2 6 8Z" fill="#fff"/></svg>SEARCH</a>
  </div>
</header>

<section class="feature" style="left:150px">
  <h3><svg width="36" height="36" viewBox="0 0 36 36"><circle cx="18" cy="18" r="14" fill="none" stroke="#1b9ce5" stroke-width="2.5"/><path d="M12 18h12M18 12v12" stroke="#1b9ce5" stroke-width="2.5"/></svg>We Hiring Now</h3>
  <p>In enim justo, rhoncus ut, imperdiet a, venenatis vitae, justo. Nullam dictum felis eu pede mollis pretium.</p>
  <a class="btn" href="#">SUBMIT RESUME</a>
</section>
<section class="feature" style="left:470px">
  <h3><svg width="36" height="36" viewBox="0 0 36 36"><circle cx="18" cy="18" r="14" fill="none" stroke="#1b9ce5" stroke-width="2.5"/><circle cx="12" cy="18" r="2" fill="#1b9ce5"/><circle cx="18" cy="18" r="2" fill="#1b9ce5"/><circle cx="24" cy="18" r="2" fill="#1b9ce5"/></svg>About VARDENHUB.NET</h3>
  <p>In enim justo, rhoncus ut, imperdiet a, venenatis vitae, justo. Nullam dictum felis eu pede mollis pretium.</p>
  <a class="btn" href="#">READ MORE</a>
</section>
<section class="feature" style="left:793px">
  <h3><svg width="36" height="36" viewBox="0 0 36 36"><circle cx="18" cy="12" r="8" fill="none" stroke="#1b9ce5" stroke-width="2.5"/><path d="M4 34c0-9 6-13 14-13s14 4 14 13" fill="none" stroke="#1b9ce5" stroke-width="2.5"/></svg>Why work with us?</h3>
  <p>In enim justo, rhoncus ut, imperdiet a, venenatis vitae, justo. Nullam dictum felis eu pede mollis pretium.</p>
  <a class="btn" href="#">READ MORE</a>
</section>

<h2 class="section-title" style="top:1074px">Featured <em>JOBS</em></h2>
<p class="section-lead" style="top:1117px">In enim justo, rhoncus ut, imperdiet a, venenatis vitae, justo. Nullam dictum felis eu pede mollis<br>pretium. Integer tincidunt. Cras dapibus. Vivamus elementum semper nisi. Aenean vulputate eleifend tellus.</p>

<article class="job" style="left:142px;top:1205px"><div class="photo" role="img" aria-label="Programmer working at a desk with monitors" style="background:linear-gradient(135deg,#c9d1d6,#6b7a85)"></div><h4>Programmers</h4><div class="tag"><i></i>Full time</div><p>In enim justo, rhoncus ut, imperdiet a, venenatis [...]</p><div class="actions"><a class="btn view" href="#">VIEW MORE</a><a class="btn" href="#">APPLY NOW</a></div></article>
<article class="job" style="left:379px;top:1205px"><div class="photo" role="img" aria-label="Hands using a tablet and laptop" style="background:linear-gradient(135deg,#9aa3a8,#4c5258)"></div><h4>iOS &amp; Android Developers</h4><div class="tag"><i></i>Full time</div><p>In enim justo, rhoncus ut, imperdiet a, venenatis [...]</p><div class="actions"><a class="btn view" href="#">VIEW MORE</a><a class="btn" href="#">APPLY NOW</a></div></article>
<article class="job" style="left:619px;top:1205px"><div class="photo" role="img" aria-label="Software engineer at computer screens" style="background:linear-gradient(135deg,#8b98a0,#3e4a50)"></div><h4>Software Engineers</h4><div class="tag"><i></i>Full time</div><p>In enim justo, rhoncus ut, imperdiet a, venenatis [...]</p><div class="actions"><a class="btn view" href="#">VIEW MORE</a><a class="btn" href="#">APPLY NOW</a></div></article>
<article class="job" style="left:856px;top:1205px"><div class="photo" role="img" aria-label="Graphic designer at a workstation" style="background:linear-gradient(135deg,#6f7fa0,#2e3346)"></div><h4>Graphic Designers</h4><div class="tag"><i></i>Full time</div><p>In enim justo, rhoncus ut, imperdiet a, venenatis [...]</p><div class="actions"><a class="btn view" href="#">VIEW MORE</a><a class="btn" href="#">APPLY NOW</a></div></article>

<article class="job" style="left:142px;top:1609px"><div class="photo" role="img" aria-label="Engineers reviewing work on a laptop" style="background:linear-gradient(135deg,#b7b2aa,#5d5750)"></div><h4>Q &amp; A Engineers</h4><div class="tag"><i></i>Full time</div><p>In enim justo, rhoncus ut, imperdiet a, venenatis [...]</p><div class="actions"><a class="btn view" href="#">VIEW MORE</a><a class="btn" href="#">APPLY NOW</a></div></article>
<article class="job" style="left:379px;top:1609px"><div class="photo" role="img" aria-label="Customer care agents wearing headsets" style="background:linear-gradient(135deg,#d9c3ae,#7e6553)"></div><h4>Customer Care Reps</h4><div class="tag"><i></i>Full time</div><p>In enim justo, rhoncus ut, imperdiet a, venenatis [...]</p><div class="actions"><a class="btn view" href="#">VIEW MORE</a><a class="btn" href="#">APPLY NOW</a></div></article>
<article class="job" style="left:619px;top:1609px"><div class="photo" role="img" aria-label="Web designer sketching layouts" style="background:linear-gradient(135deg,#e4e6e8,#9aa0a6)"></div><h4>Web Designers</h4><div class="tag"><i></i>Full time</div><p>In enim justo, rhoncus ut, imperdiet a, venenatis [...]</p><div class="actions"><a class="btn view" href="#">VIEW MORE</a><a class="btn" href="#">APPLY NOW</a></div></article>
<article class="job" style="left:856px;top:1609px"><div class="photo" role="img" aria-label="Photographer holding a camera" style="background:linear-gradient(135deg,#7a6e66,#2b2623)"></div><h4>Photographers</h4><div class="tag"><i></i>Full time</div><p>In enim justo, rhoncus ut, imperdiet a, venenatis [...]</p><div class="actions"><a class="btn view" href="#">VIEW MORE</a><a class="btn" href="#">APPLY NOW</a></div></article>

<section class="cta">
  <p>Add your resume and let your next job find you.</p>
  <a class="btn" href="#" style="background:none">ADD RESUME</a>
</section>

<section class="quote">
  <div class="quote-photo" role="img" aria-label="Smiling man working at a laptop in a café"></div>
  <div class="quote-shade"></div>
  <div class="avatar" role="img" aria-label="Portrait of the quoted client"></div>
  <p>Lorem ipsum dolor sit amet consecsed a do eiusmod temp incidunt olore magna aliqu Lorem ipsum dolor sit amet et dincidunt ut labore et dolore magna aliqu Lorem ipsaliqu.</p>
  <div class="who">- Marta Linwood</div>
  <div class="dots"><span></span><span class="on"></span><span></span></div>
</section>

<h2 class="section-title" style="top:2703px">Latest News from <em>VARDENHUB.NET</em></h2>
<p class="section-lead" style="top:2749px">In enim justo, rhoncus ut, imperdiet a, venenatis vitae, justo. Nullam dictum felis eu pede mollis<br>pretium. Integer tincidunt. Cras dapibus. Vivamus elementum semper nisi. Aenean vulputate eleifend tellus.</p>

<article class="news" style="left:125px;top:2827px"><div class="photo" role="img" aria-label="Business people signing documents at a desk" style="background:linear-gradient(135deg,#eef1f3,#a9b2b8)"></div><div class="meta"><div class="date">Sep 25,<br>2017</div><div class="excerpt">Etiam ultricies nisi vel augue. Curabitur ullamcorper ultricies tellus eget condimentum nisl.</div></div></article>
<article class="news" style="left:611px;top:2827px"><div class="photo" role="img" aria-label="Smiling team gathered around a laptop" style="background:linear-gradient(135deg,#e9e4dc,#9b8f80)"></div><div class="meta"><div class="date">Aug 11,<br>2017</div><div class="excerpt">Etiam ultricies nisi vel augue. Curabitur ullamcorper ultricies tellus eget condimentum nisl.</div></div></article>

<footer class="footer">
  <h5 class="abs" style="left:150px;top:74px">Subscribe to our Newsletter</h5>
  <div class="news-input">Your email address</div>
  <a class="btn news-btn" href="#"><svg width="14" height="12" viewBox="0 0 16 14"><path d="M0 6 16 0 12 14 8 9 14 2 6 8Z" fill="#fff"/></svg>SUBSCRIBE</a>
  <h5 class="abs" style="left:536px;top:74px">Follow us on</h5>
  <div class="footer-socials"><span></span><span></span><span></span><span></span><span></span></div>
  <h5 class="abs" style="left:820px;top:74px">Need Help?</h5>
  <div class="abs" style="left:820px;top:116px;color:#fff;font-size:13px;white-space:nowrap">&#9990; CALL US: <b style="font-size:19px;font-weight:600">1800-0000-5678</b></div>
  <div class="footer-rule"></div>

  <div class="abs" style="left:150px;top:222px;display:flex;align-items:center;gap:8px;font-size:36px;font-weight:700;color:var(--blue)">VARDEN<span style="width:22px;height:22px;border-radius:50%;background:var(--blue)"></span></div>
  <p class="abs" style="left:150px;top:282px;width:200px;font-size:12.5px;line-height:25px;color:#fff">Lorem ipsum dolor sit amet, consectetur adipiscing elit. Cras orci sem, vulputate sit amet ipsum vel, pellentesque varius nunc. Mauris non vulputate augue, nulla ligula.</p>

  <h6 class="abs" style="left:408px;top:224px">Information</h6>
  <ul class="links" style="left:412px"><li>About Us</li><li class="hl">Help Desk</li><li>Support</li><li>Privacy Policy</li><li>Terms &amp; Conditions</li></ul>
  <h6 class="abs" style="left:612px;top:224px">Useful Links</h6>
  <ul class="links" style="left:612px"><li>Home</li><li>Search Job</li><li>Positions</li><li>Latest News</li><li class="hl">Jobs</li></ul>
  <h6 class="abs" style="left:822px;top:224px">Get in Touch</h6>
  <div class="contact-field" style="top:262px">Name</div>
  <div class="contact-field" style="top:305px">Email address</div>
  <div class="contact-field" style="top:348px;height:60px">Message</div>
  <a class="btn abs" href="#" style="left:1017px;top:348px;width:42px;height:60px"><svg width="16" height="14" viewBox="0 0 16 14"><path d="M0 6 16 0 12 14 8 9 14 2 6 8Z" fill="#fff"/></svg></a>

  <p class="copyright">Varden Hub Copyright © 2017. All rights reserved.</p>
</footer>

</body>
</html>
```